Little Maple Nest - Daycare and Childcare

We are a daycare / Childcare business and are looking to make business cards to distribute. Our website to give you a better idea of what we do and the style design is: littlemaplenestdalewick.example. Our four keystones that we focus on are "educational, affordable, creative, nurturing" these may be used with symbols or icons (just an idea) we want a fun but not overwhelming design to the cards. If you need additional questions about this project feel free to call me at: 555-613-4471

Target Market(s)

Parents needed daycare/childcare services

Industry/Entity Type

Preschool

Contact Information for Business Card

Title: Little-maple Nest
Preschool & childcare

Contact Info:
Phone: 555-738-1926
Address: 482 N 700 W, Bountiful, UT
Website: www.littlemaplenestdalewick.example

Font styles to use
Other font styles liked:
• Fun font if it looks good

Requirements
Must have
• Title & contact Info
Nice to have
• Fun & friendly feel. Pictures or diagrams - get ideas form our website (www.littlemaplenestdalewick.example)
Should not have
• -Pictures of real people
• -contact names

```html
<!DOCTYPE html>
<html lang="en">
<head>
<meta charset="utf-8">
<title>Little-maple Nest – Business Card</title>
<link rel="stylesheet" href="https://fonts.googleapis.com/css2?family=Sniglet:wght@400;800&family=Delius&display=swap">
<style>
  :root {
    --bg: #e6e6e6;
    --card: #ffffff;
    --red: #e8262b;
    --orange: #f28a1e;
    --yellow: #f7c51e;
    --green: #1f9a48;
    --blue: #2b3f9e;
    --purple: #7b3b96;
    --pink: #e5407f;
    --sky: #3aa6dd;
    --ink-blue: #2a3a9c;
  }
  * { box-sizing: border-box; margin: 0; padding: 0; }
  html, body { width: 1200px; height: 898px; overflow: hidden; }
  body { background: var(--bg); position: relative; font-family: "Delius", cursive; }

  .card {
    position: absolute; left: 75px; top: 149px;
    width: 1050px; height: 600px;
    background: var(--card);
    box-shadow: 0 10px 30px rgba(0,0,0,.25);
    overflow: hidden;
  }
  .stripes-top {
    position: absolute; left: 0; top: 0; width: 100%; height: 72px;
    background: repeating-linear-gradient(180deg,
      var(--orange) 0 5px, var(--card) 5px 8px,
      var(--red) 8px 13px, var(--card) 13px 16px,
      var(--yellow) 16px 21px, var(--card) 21px 24px,
      var(--purple) 24px 29px, var(--card) 29px 32px,
      var(--blue) 32px 37px, var(--card) 37px 40px,
      var(--green) 40px 45px, var(--card) 45px 48px);
  }
  .illustration {
    position: absolute; left: 40px; top: 92px; width: 500px; height: 350px;
    border-radius: 18px;
    background: linear-gradient(160deg, #f6d6ea 0%, #fcf1b4 35%, #cfe8f6 65%, #e3d3ef 100%);
  }
  .title {
    position: absolute; left: 560px; top: 104px; width: 470px;
    font-family: "Sniglet", cursive; font-weight: 800;
    font-size: 46px; line-height: 1; color: var(--red);
    text-align: center; white-space: nowrap;
  }
  .subtitle {
    position: absolute; left: 560px; top: 170px; width: 470px;
    font-family: "Sniglet", cursive; font-weight: 800;
    font-size: 30px; line-height: 1; color: var(--ink-blue);
    text-align: center; white-space: nowrap;
  }
  .contact-pill {
    position: absolute; height: 58px; border-radius: 29px;
    display: flex; align-items: center; padding-left: 66px;
    font-size: 27px; white-space: nowrap;
  }
  .contact-pill.phone { left: 600px; top: 240px; width: 380px; background: var(--red); color: var(--yellow); }
  .contact-pill.address { left: 590px; top: 336px; width: 450px; background: var(--yellow); color: var(--ink-blue); }
  .contact-icon {
    position: absolute; left: -20px; top: -9px; width: 76px; height: 76px; border-radius: 50%;
    display: flex; align-items: center; justify-content: center;
  }
  .phone .contact-icon { background: var(--blue); border: 5px solid var(--yellow); }
  .address .contact-icon { background: var(--green); border: 5px solid var(--card); }
  .contact-icon svg { width: 38px; height: 38px; }

  .stripes-bottom {
    position: absolute; left: 0; top: 448px; width: 100%; height: 152px;
    background: repeating-linear-gradient(180deg,
      var(--red) 0 5px, var(--card) 5px 8px,
      var(--purple) 8px 13px, var(--card) 13px 16px,
      var(--pink) 16px 21px, var(--card) 21px 24px);
  }
  .web-band {
    position: absolute; left: 0; top: 476px; width: 100%; height: 74px;
    background: var(--blue);
    display: flex; align-items: center; justify-content: center;
    font-size: 40px; color: var(--card); letter-spacing: 1px; white-space: nowrap;
  }
  .stripes-base {
    position: absolute; left: 0; top: 550px; width: 100%; height: 50px;
    background: repeating-linear-gradient(180deg,
      var(--green) 0 5px, var(--sky) 5px 10px,
      var(--blue) 10px 15px, var(--purple) 15px 20px);
  }
</style>
</head>
<body>
  <section class="card">
    <div class="stripes-top"></div>
    <div class="illustration" role="img" aria-label="Cartoon children holding hands beneath speech bubbles reading Learn, Play, Explore, Create and Giggle"></div>

    <h1 class="title">Little-maple Nest</h1>
    <p class="subtitle">Preschool &amp; childcare</p>

    <div class="contact-pill phone">
      <span class="contact-icon">
        <svg viewBox="0 0 24 24"><path fill="#f7c51e" d="M6.6 10.8a15.1 15.1 0 0 0 6.6 6.6l2.2-2.2a1 1 0 0 1 1-.25 11.4 11.4 0 0 0 3.6.57 1 1 0 0 1 1 1V20a1 1 0 0 1-1 1A17 17 0 0 1 3 4a1 1 0 0 1 1-1h3.5a1 1 0 0 1 1 1c0 1.25.2 2.450.57 3.57a1 1 0 0 1-.25 1z"/></svg>
      </span>
      555-738-1926
    </div>

    <div class="contact-pill address">
      <span class="contact-icon">
        <svg viewBox="0 0 24 24"><path fill="#ffffff" d="M12 2a7 7 0 0 0-7 7c0 5.2 7 13 7 13s7-7.8 7-13a7 7 0 0 0-7-7zm0 9.5A2.5 2.5 0 1 1 12 6.5a2.5 2.5 0 0 1 0 5z"/></svg>
      </span>
      482 N 700 W, Bountiful, UT
    </div>

    <div class="stripes-bottom"></div>
    <div class="web-band">www.littlemaplenestdalewick.example</div>
    <div class="stripes-base"></div>
  </section>
</body>
</html>
```